Personal Travel Advisor needs Business Cards

UPDATED INFORMATION:
I have attached a sample of the script I would to use for "Travel"
Specialties are updated to: Culinary & Wine, Golf, Food, Cruising, River Cruising

I need a business card for my new company - Lena Orwick Travel - which I can also use as a logo.

I specialize in culinary & wine, golf, river cruising, select destinations and group travel.
The design should convey the value of my expertise and personalized services.

Target Market(s)

Target market is varied but most likely will be 40+ years.

I need to build a client base so need to be inclusive, but would like to draw in affluent travelers who value their time, and my expertise.

Groups can be any demographic - groups of golfers, wine club, sports fan trips, etc.

Industry/Entity Type

Business

Requirements
Must have
• Must find a non- prominent way to display the following information:

"Affiliated as an independent contractor with Bellhaven Travel"
and
"CST #4637215-84"

Nice to have
• The design should be striking but elegant with a modern look and feel

One side of the card could be in a solid color or black?

I like the idea of Lena Orwick being in a font and Travel being in a handwritten script...but I do not want this idea to inhibit your design.
Should not have
• I do not want any ships, planes, or other typical travel illustrations in the design.

```html
<!DOCTYPE html>
<html lang="en">
<head>
<meta charset="utf-8">
<title>Lena Orwick Travel — Business Card</title>
<link rel="stylesheet" href="https://fonts.googleapis.com/css2?family=Quicksand:wght@300;400;500;600&family=Parisienne&display=swap">
<style>
  :root {
    --brand-blue: #0b4f9f;
    --leaf-green: #8dbb3a;
    --pale-green: #d4e59c;
    --blush: #e6cfd6;
    --moss: #6f9a3a;
    --white: #ffffff;
    --page: #ffffff;
  }
  * { box-sizing: border-box; margin: 0; padding: 0; }
  html, body { width: 800px; height: 1200px; overflow: hidden; background: var(--page); }
  body { position: relative; font-family: "Quicksand", sans-serif; color: var(--brand-blue); }

  .card {
    position: absolute; left: 22px; width: 754px; overflow: hidden;
    box-shadow: 3px 3px 4px rgba(0,0,0,0.35);
  }
  .card--front { top: 29px; height: 415px; background: var(--brand-blue); }
  .card--back { top: 475px; height: 410px; }

  /* Front */
  .front-photo {
    position: absolute; inset: 0 0 auto 0; height: 270px;
    background:
      radial-gradient(ellipse at 75% 30%, rgba(255,255,255,0.35), transparent 45%),
      linear-gradient(100deg, #d8d1b4 0%, #e3c7c9 22%, #a9c46a 48%, #7fab3c 72%, #4f7a2a 100%);
  }
  .front-bands { position: absolute; inset: 0; width: 754px; height: 415px; }
  .wordmark {
    position: absolute; left: 113px; top: 50px;
    color: var(--white); font-weight: 500; font-size: 44px; line-height: 1.1;
    letter-spacing: -0.5px;
  }
  .wordmark span { display: block; }
  .wordmark .wordmark-sub { padding-left: 90px; font-size: 38px; }
  .tagline {
    position: absolute; left: 0; right: 0; top: 286px; text-align: center;
    color: var(--white); font-weight: 500; font-size: 24px; letter-spacing: 0.4px;
  }
  .affiliation {
    position: absolute; left: 8px; right: 10px; top: 380px;
    display: flex; align-items: center; justify-content: space-between;
    color: var(--white); font-weight: 500; font-size: 14.5px; letter-spacing: 0.3px;
  }
  .affiliation-mark { display: flex; align-items: center; gap: 6px; }
  .affiliation-mark .rule { width: 30px; height: 1.5px; background: var(--white); opacity: 0.85; }
  .affiliation-mark .dot { width: 22px; height: 22px; border-radius: 50%; background: #0a2f66; border: 1px solid rgba(255,255,255,0.6); }

  /* Back */
  .back-photo {
    position: absolute; inset: 0;
    background:
      radial-gradient(ellipse at 90% 35%, rgba(141,187,58,0.9), transparent 45%),
      radial-gradient(ellipse at 20% 75%, #e9d2dc, transparent 55%),
      linear-gradient(100deg, #e7d8cf 0%, #e6d0d6 35%, #cfc9a6 65%, #93b04c 100%);
  }
  .back-shapes { position: absolute; inset: 0; width: 754px; height: 410px; }
  .advisor-name {
    position: absolute; left: 252px; top: 22px;
    color: var(--white); font-weight: 500; font-size: 29px; letter-spacing: -0.3px;
  }
  .advisor-title {
    position: absolute; left: 316px; top: 62px;
    color: var(--brand-blue); font-weight: 300; font-size: 23px;
  }
  .section-heading {
    position: absolute; top: 100px; transform: translateX(-50%);
    font-family: "Parisienne", cursive; font-size: 30px; color: var(--brand-blue);
    border-bottom: 2px solid var(--white); padding: 0 4px 1px; line-height: 1.3;
    text-shadow: 0 0 1px var(--white);
  }
  .section-heading--expertise { left: 152px; }
  .section-heading--contact { left: 570px; }
  .divider {
    position: absolute; left: 359px; top: 135px; width: 2px; height: 220px;
    background: linear-gradient(180deg, transparent, var(--white) 15%, var(--white) 85%, transparent);
  }
  .expertise-list { list-style: none; position: absolute; left: 8px; top: 165px; }
  .expertise-list li {
    display: flex; align-items: center; gap: 6px; height: 40px;
    font-size: 23px; font-weight: 500; color: var(--brand-blue);
  }
  .expertise-list svg { width: 24px; height: 20px; flex: none; }
  .contact-list { list-style: none; position: absolute; left: 410px; top: 162px; }
  .contact-list li { height: 64px; font-size: 22px; font-weight: 500; color: var(--brand-blue); }
</style>
</head>
<body>

<section class="card card--front" aria-label="Card front">
  <div class="front-photo" role="img" aria-label="Soft-focus photograph of a dandelion seed against a green and blush background"></div>
  <svg class="front-bands" viewBox="0 0 754 415" aria-hidden="true">
    <path d="M0 232 Q377 214 754 240 L754 415 L0 415 Z" fill="var(--pale-green)"/>
    <path d="M0 258 Q377 236 754 270 L754 415 L0 415 Z" fill="var(--white)"/>
    <path d="M0 262 Q377 242 754 274 L754 415 L0 415 Z" fill="var(--brand-blue)"/>
  </svg>
  <h1 class="wordmark"><span>Lena Orwick</span><span class="wordmark-sub">Travel</span></h1>
  <p class="tagline">Research, plan and book your travel with an expert’s help.</p>
  <p class="affiliation">
    <span>Affiliated as an independent contractor with Bellhaven Travel.</span>
    <span class="affiliation-mark"><span class="rule"></span><span class="dot"></span><span class="rule"></span></span>
    <span>CST #4637215-84</span>
  </p>
</section>

<section class="card card--back" aria-label="Card back">
  <div class="back-photo" role="img" aria-label="Blurred soft background in blush and green tones"></div>
  <svg class="back-shapes" viewBox="0 0 754 410" aria-hidden="true">
    <path d="M0 0 L200 0 Q80 60 0 165 Z" fill="var(--pale-green)" opacity="0.85"/>
    <path d="M754 185 L754 410 L633 410 Q700 300 754 185 Z" fill="var(--brand-blue)"/>
  </svg>
  <h2 class="advisor-name">Lena Orwick</h2>
  <p class="advisor-title">personal travel advisor</p>

  <h3 class="section-heading section-heading--expertise">Expertise</h3>
  <h3 class="section-heading section-heading--contact">Contact</h3>
  <div class="divider"></div>

  <ul class="expertise-list">
    <li><svg viewBox="0 0 24 20"><path d="M1 11 L8 18 L23 2 L8 13 Z" fill="var(--brand-blue)"/></svg>Culinary &amp; Wine</li>
    <li><svg viewBox="0 0 24 20"><path d="M1 11 L8 18 L23 2 L8 13 Z" fill="var(--brand-blue)"/></svg>Golf</li>
    <li><svg viewBox="0 0 24 20"><path d="M1 11 L8 18 L23 2 L8 13 Z" fill="var(--brand-blue)"/></svg>Food</li>
    <li><svg viewBox="0 0 24 20"><path d="M1 11 L8 18 L23 2 L8 13 Z" fill="var(--brand-blue)"/></svg>Cruising</li>
    <li><svg viewBox="0 0 24 20"><path d="M1 11 L8 18 L23 2 L8 13 Z" fill="var(--brand-blue)"/></svg>River Cruising</li>
  </ul>

  <ul class="contact-list">
    <li>Address:</li>
    <li>Phone:</li>
    <li>E-mail:</li>
  </ul>
</section>

</body>
</html>
```